Construction material supplies company business card ****

1. Full company name “K R Mortar Works Ltd”
I am after a Business card design for the company as a whole. We are better known in Solomon Islands as “K R Mortar” for short.

We are a building materials supplier of
Ready Mixed Concrete, Bricks and Blocks,
Quarry products- gravel, aggregates, sand etc.
Cement distributor/retailer of reputable brands.
Other prefab concrete products. Culverts, wave breakers, concrete retaining blocks etc.

2. Competitive Advantage over Competition: Quality, efficient, professional, dependable, reliable

3. We want people to feel trust worthy, high quality, strong when they see our brand

5. No preference to color. Maybe more sturdy and corporate. Not fancy.

Industry/Entity Type

CONSTRUCTION SUPPLY

Contact Information for Business Card

Name, Position, office phone mob phone, email

Requirements
Must have
• the company logo
Nice to have
• would like to see a mixture of designs, of with logo only and also with simple graphic designs to bring out the company whilst still have the strong sturdy professional feeling

```html
<!DOCTYPE html>
<html lang="en">
<head>
<meta charset="UTF-8">
<title>K R Mortar – Business Card</title>
<link href="https://fonts.googleapis.com/css2?family=Montserrat:ital,wght@0,400;0,600;0,700;1,400&display=swap" rel="stylesheet">
<style>
  :root {
    --navy: #163f66;
    --navy-deep: #0f3050;
    --navy-light: #1f5a8c;
    --accent: #2a78c0;
    --paper: #ffffff;
    --ink: #3a4350;
    --stage: #1b1c1e;
  }
  * { margin: 0; padding: 0; box-sizing: border-box; }
  html, body {
    width: 1200px; height: 900px; overflow: hidden;
    background: var(--stage);
    font-family: "Montserrat", Arial, sans-serif;
  }
  .card {
    position: absolute; left: 300px;
    width: 600px; height: 343px;
    border-radius: 22px; overflow: hidden;
    box-shadow: 0 10px 30px rgba(0,0,0,.5);
  }
  .card-front { top: 70px; background: var(--paper); }
  .card-back { top: 487px; background: var(--navy); }

  .brand {
    position: absolute; display: flex; align-items: center; gap: 12px;
    font-weight: 700; letter-spacing: 3px; text-transform: uppercase;
  }
  .brand-mark { width: 22px; height: 22px; }
  .card-front .brand { left: 44px; top: 42px; font-size: 26px; color: var(--navy); }
  .card-front .brand-mark { background: var(--navy); }

  .divider {
    position: absolute; left: 44px; right: 0; top: 196px;
    height: 1px; background: var(--navy);
  }
  .edge-tab {
    position: absolute; right: 0; top: 182px;
    width: 12px; height: 28px; background: var(--navy);
  }

  .person { position: absolute; right: 56px; top: 140px; text-align: right; }
  .person-name {
    font-size: 22px; font-weight: 600; color: var(--navy);
    letter-spacing: 1.5px; text-transform: uppercase;
  }
  .person-role { font-size: 14px; color: var(--ink); margin-top: 2px; }

  .contacts { position: absolute; left: 44px; top: 224px; list-style: none; }
  .contacts li {
    display: flex; align-items: center; gap: 8px;
    font-size: 13px; color: var(--ink); line-height: 22px;
  }
  .contacts svg { width: 12px; height: 12px; fill: none; stroke: var(--navy); stroke-width: 2; }

  .pattern-fill {
    position: absolute; inset: 0;
    background: linear-gradient(135deg, var(--navy-light) 0%, var(--navy) 45%, var(--navy-deep) 100%);
  }
  .card-back .brand {
    left: 50%; top: 50%; transform: translate(-50%, -50%);
    font-size: 34px; color: var(--paper);
  }
  .card-back .brand-mark { width: 28px; height: 28px; background: var(--paper); }
</style>
</head>
<body>
  <section class="card card-front">
    <div class="brand"><span class="brand-mark"></span>K R Mortar</div>
    <div class="person">
      <div class="person-name">Daniel Hart</div>
      <div class="person-role">President</div>
    </div>
    <div class="divider"></div>
    <div class="edge-tab"></div>
    <ul class="contacts">
      <li><svg viewBox="0 0 24 24"><path d="M5 3h4l2 5-3 2a12 12 0 0 0 6 6l2-3 5 2v4a2 2 0 0 1-2 2A18 18 0 0 1 3 5a2 2 0 0 1 2-2z"/></svg>555-214-7380</li>
      <li><svg viewBox="0 0 24 24"><rect x="2" y="5" width="20" height="14"/><path d="M2 5l10 8 10-8"/></svg>info@KRMortar.com</li>
      <li><svg viewBox="0 0 24 24"><circle cx="12" cy="12" r="10"/><path d="M2 12h20M12 2a15 15 0 0 1 0 20M12 2a15 15 0 0 0 0 20"/></svg>www.KRMortar.com</li>
    </ul>
  </section>

  <section class="card card-back">
    <div class="pattern-fill" role="img" aria-label="Repeating embossed brand pattern in blue tones"></div>
    <div class="brand"><span class="brand-mark"></span>K R Mortar</div>
  </section>
</body>
</html>
```